Manufacturer's Representative Group needs a clean new Website

We represent and sell a number of suppliers that design and build products used in Biopharmaceutical manufacturing. Our sales region is in the central US. Our customer base is scientific / engineering based - so clean, we organized design with a focus on the products - easy and clear navigation is necessary. We do not sell direct or warehouse product - so e-commerce is not needed. Our customers will use the website for reference on what we do and offer - we will use the site as a platform to present products from each vendor and the home page will be used to capture an overview and draw users deeper into the site. You can view our current site - which needs A LOT of help to get ideas on products represented and types of products

Target Market(s)

Engineers and Pharmaceutical / Bio pharm end users

Industry/Entity Type

E-Commerce

Number of Pages Required

2 page

Font styles to use
Sans Serif

Requirements
Must have
• I need a home page that provides a snapshot of my company and the product lines we represent - then a second page that I can copy as a template for each line I rep as well as for an "About us / contact" page.
• I would like to be able to manage content on the pages so something easy to adjust pictures or add content is a must
• Must use our logo

```html
<!DOCTYPE html>
<html lang="en">
<head>
<meta charset="utf-8">
<title>Prairie Bio — Home</title>
<link href="https://fonts.googleapis.com/css2?family=Lato:ital,wght@0,400;0,700;1,400&display=swap" rel="stylesheet">
<style>
:root{
  --navy:#2b2a6e;
  --navy-deep:#2a2660;
  --orange:#f15a22;
  --ink:#333;
  --muted:#555;
  --line:#c9c9d6;
  --panel:#f4f4f4;
  --white:#fff;
  --black:#0b0b0b;
}
*{box-sizing:border-box;margin:0;padding:0}
html,body{width:1200px;height:2426px;overflow:hidden}
body{font-family:'Lato',sans-serif;color:var(--ink);background:var(--white);position:relative}
.abs{position:absolute}
.header{left:0;top:0;width:1200px;height:89px;background:linear-gradient(#fff,#f1f1f1)}
.brand{left:130px;top:28px;display:flex;align-items:center;gap:14px;font-size:42px;font-weight:400;color:var(--navy);line-height:1}
.brand .dot{width:34px;height:34px;border-radius:50%;background:var(--orange)}
.phone{left:900px;top:8px;font-size:23px;color:var(--ink);display:flex;align-items:center;gap:6px}
.nav{left:511px;top:48px;width:556px;height:41px;background:var(--navy);border-radius:4px 4px 0 0;display:flex;align-items:center;padding:0 10px}
.nav a{color:#fff;text-decoration:none;font-size:15px;font-weight:700;padding:0 26px;border-right:1px solid #5b5a95;height:26px;line-height:26px}
.nav a:last-child{border-right:0}
.nav a.active{background:var(--orange);border-radius:3px;padding:0 16px;margin-right:14px;border-right:0}
.hero{left:0;top:89px;width:1200px;height:458px;background:linear-gradient(120deg,#8d8e88 0%,#b7b9b4 35%,#d9dbd8 60%,#9aa0a0 100%)}
.band{left:0;top:547px;width:1200px;height:56px;background:var(--orange)}
.band p{position:absolute;left:130px;top:14px;color:#fff;font-weight:700;font-size:24px}
.dots{position:absolute;left:1014px;top:22px;display:flex;gap:4px}
.dots i{width:13px;height:13px;border-radius:50%;background:#fff;border:2px solid var(--navy)}
.welcome{left:0;top:603px;width:1200px;height:294px;background:var(--panel)}
.products{left:0;top:897px;width:1200px;height:510px;background:#efefef}
.title{position:absolute;left:0;width:1200px;text-align:center;color:var(--navy);font-weight:700;font-size:29px}
.rule{position:absolute;left:490px;width:220px;height:14px}
.lead{position:absolute;left:137px;width:926px;text-align:center;font-size:13.5px;line-height:22px;color:var(--ink)}
.btn{position:absolute;background:var(--orange);color:#fff;font-weight:700;text-align:center;border-radius:2px}
.card{position:absolute;top:1004px;width:215px;height:372px;background:#fff;border:1px solid #d6d6d6;border-radius:3px;text-align:center}
.card .shot{height:189px;margin:0;border-bottom:1px solid #ddd}
.card h3{font-weight:400;font-size:19px;color:var(--navy);margin-top:14px}
.card p{font-size:14px;line-height:22px;color:var(--ink);margin:12px 22px 0}
.card .btn{left:48px;top:323px;width:118px;height:32px;line-height:32px;font-size:15px}
.carousel{left:131px;top:1557px;width:936px;height:109px;background:#fff;border:2px solid #d4d4d4}
.partner{position:absolute;top:36px;font-size:26px;font-weight:700;color:var(--navy)}
.arrow{position:absolute;top:1604px;width:16px;height:16px;border-radius:50%;background:#ddd}
.h2{position:absolute;font-size:29px;font-weight:700;color:var(--navy)}
.news{position:absolute;top:1774px;width:190px}
.news .shot{width:170px;height:102px;border:1px solid #ccc}
.news h4{font-size:14px;font-weight:700;color:var(--navy);margin-top:16px}
.news .date{font-size:14px;margin-top:6px;color:var(--black)}
.news p{font-size:13.5px;line-height:20px;margin-top:4px}
.news a{display:block;margin-top:8px;color:var(--orange);font-style:italic;font-size:13.5px;text-decoration:none}
.field{position:absolute;left:817px;width:250px;border:1px solid #bbb;border-radius:3px;background:#fff;font-size:13px;color:#aaa;padding:9px 12px}
.testimonials{left:0;top:2023px;width:1200px;height:267px;background:linear-gradient(90deg,#5d5f9a,#7b7eb2 45%,#6a6ca4)}
.testimonials .txt{position:absolute;color:#fff}
.footer{left:0;top:2290px;width:1200px;height:103px;background:var(--navy-deep);color:#fff;font-size:13px}
.copy{left:0;top:2393px;width:1200px;height:33px;background:var(--black);color:#fff;font-size:12.5px;text-align:center;line-height:33px}
.soc{position:absolute;top:2320px;width:32px;height:32px;border-radius:50%;border:2px solid #fff}
</style>
</head>
<body>

<header class="abs header">
  <div class="abs brand"><span class="dot"></span>Prairie Bio</div>
  <div class="abs phone">
    <svg width="26" height="26" viewBox="0 0 26 26"><circle cx="13" cy="13" r="11" fill="none" stroke="#f15a22" stroke-width="2"/><path d="M9 7l3 3-2 2c1 2 2 3 4 4l2-2 3 3-2 2c-5 0-10-5-10-10z" fill="#f15a22"/></svg>
    123-456-7890
  </div>
  <nav class="abs nav">
    <a class="active">Home</a><a>About</a><a>Product</a><a>Contact Us</a><a>Request Quote</a>
  </nav>
</header>

<div class="abs hero" role="img" aria-label="Photo of a technician in a white cleanroom suit working at laboratory equipment"></div>
<div class="abs band"><p>Prairiebio Testing for you Best Qulity Product every day</p><div class="dots"><i></i><i></i><i></i></div></div>

<section class="abs welcome">
  <h2 class="title" style="top:36px">Welcome to Prairie Bio</h2>
  <svg class="rule" style="top:82px" viewBox="0 0 220 14"><line x1="0" y1="7" x2="220" y2="7" stroke="#c9c9d6"/><circle cx="110" cy="7" r="5" fill="#fff" stroke="#c9c9d6"/></svg>
  <p class="lead" style="top:109px">Lorem ipsum dolor sit amet, consectetuer adipiscing elit, sed diam nonummy nibh euismod tincidunt ut laoreet dolore magna aliquam erat volutpat. Ut wisi enim ad minim veniam, quis nostrud exerci tation ullamcorper suscipit lobortis nisl ut aliquip ex ea commodo consequat. Duis autem vel eum iriure dolor in hendrerit in vulputate velit esse molestie consequat, vel illum dolore eu feugiat nulla facilisis at vero eros et accumsan et iusto odio dignissim qui blandit praesent luptatum zzril delenit augue duis dolore te feugait nulla facilisi.</p>
  <div class="btn" style="left:535px;top:214px;width:146px;height:40px;line-height:40px;font-size:16px">Read More</div>
</section>

<section class="abs products">
  <h2 class="title" style="top:22px">Our Product</h2>
  <svg class="rule" style="top:62px" viewBox="0 0 220 14"><line x1="0" y1="7" x2="220" y2="7" stroke="#c9c9d6"/><circle cx="110" cy="7" r="5" fill="#fff" stroke="#c9c9d6"/></svg>
</section>

<article class="card" style="left:131px"><div class="shot" role="img" aria-label="Photo of a stainless steel cleanroom cabinet" style="background:linear-gradient(#d8dde0,#9ea6ab)"></div><h3>Vivamus Tincidunt</h3><p>Lorem ipsum dolor consectetur adipiscing elit estibueff</p><div class="btn">Read More››</div></article>
<article class="card" style="left:372px"><div class="shot" role="img" aria-label="Photo of a blue peristaltic pump" style="background:linear-gradient(#9fb4d6,#3d5f9c)"></div><h3>Curabitur Pharetra</h3><p>Lorem ipsum dolor consectetur adipiscing elit estibueff</p><div class="btn">Read More››</div></article>
<article class="card" style="left:612px"><div class="shot" role="img" aria-label="Photo of clear tubing coils on a teal background" style="background:linear-gradient(135deg,#1d9ab0,#bfe8ef)"></div><h3>Maecenas Ultricies</h3><p>Lorem ipsum dolor consectetur adipiscing elit estibueff</p><div class="btn">Read More››</div></article>
<article class="card" style="left:853px"><div class="shot" role="img" aria-label="Photo of a red benchtop pump" style="background:linear-gradient(#e8e8e8,#c4302a)"></div><h3>Malesuada Euismod</h3><p>Lorem ipsum dolor consectetur adipiscing elit estibueff</p><div class="btn">Read More››</div></article>

<h2 class="title" style="top:1426px">Companies Represented</h2>
<svg class="rule" style="top:1472px" viewBox="0 0 220 14"><line x1="0" y1="7" x2="220" y2="7" stroke="#c9c9d6"/><circle cx="110" cy="7" r="5" fill="#fff" stroke="#c9c9d6"/></svg>
<p class="lead" style="top:1497px">Lorem ipsum dolor sit amet, consectetuer adipiscing elit, sed diam nonummy nibh euismod tincidunt ut laoreet dolore magna aliquam erat volutpat. Ut wisi enim ad minim veniam, quis nostrud exerci tation ullamcorper.</p>
<div class="abs carousel">
  <span class="partner" style="left:40px">Harlan Flow</span>
  <span class="partner" style="left:270px">CleanSeal</span>
  <span class="partner" style="left:490px">Verdan Plastics</span>
  <span class="partner" style="left:760px">Q-Form</span>
</div>
<span class="arrow" style="left:124px"></span><span class="arrow" style="left:1059px"></span>

<h2 class="h2" style="left:131px;top:1700px">Latest News</h2>
<svg class="abs" style="left:131px;top:1749px" width="626" height="14"><line x1="0" y1="7" x2="626" y2="7" stroke="#c9c9d6"/><circle cx="10" cy="7" r="5" fill="#fff" stroke="#c9c9d6"/></svg>
<div class="news" style="left:131px"><div class="shot" role="img" aria-label="Photo of a sample container" style="background:linear-gradient(#e6e6dc,#a9a99a)"></div><h4>Lorem ipsum dolor sit amet</h4><div class="date">Dec 23, 2014</div><p>Utwisi enim ad m venialj quisa nostrud exe ullamcoer.</p><a>Read More ››</a></div>
<div class="news" style="left:356px"><div class="shot" role="img" aria-label="Photo of a plastic bottle" style="background:linear-gradient(#d4d4d4,#bdbdbd)"></div><h4>Lorem ipsum dolor sit amet</h4><div class="date">Dec 24, 2014</div><p>Utwisi enim ad m venialj quisa nostrud exe ullamcoer.</p><a>Read More ››</a></div>
<div class="news" style="left:581px"><div class="shot" role="img" aria-label="Photo of clear bottles" style="background:linear-gradient(#eef0f4,#b8bfd0)"></div><h4>Lorem ipsum dolor sit amet</h4><div class="date">Dec 25, 2014</div><p>Utwisi enim ad m venialj quisa nostrud exe ullamcoer.</p><a>Read More ››</a></div>

<h2 class="h2" style="left:817px;top:1700px">Quick Contact</h2>
<svg class="abs" style="left:817px;top:1749px" width="250" height="14"><line x1="0" y1="7" x2="250" y2="7" stroke="#c9c9d6"/><circle cx="10" cy="7" r="5" fill="#fff" stroke="#c9c9d6"/></svg>
<div class="field" style="top:1774px;height:37px">Name</div>
<div class="field" style="top:1820px;height:37px">Email</div>
<div class="field" style="top:1866px;height:78px">Message</div>
<div class="abs" style="left:864px;top:1953px;width:160px;height:33px;background:var(--navy);color:#fff;font-weight:700;font-size:16px;text-align:center;line-height:33px;border-radius:2px">Submit</div>

<section class="abs testimonials" role="img" aria-label="Blue-tinted photo of process equipment in a lab">
  <h2 class="txt" style="left:0;width:1200px;top:34px;text-align:center;font-size:29px;font-weight:700">What our Customers Say</h2>
  <svg class="abs" style="left:490px;top:80px" width="220" height="14"><line x1="0" y1="7" x2="220" y2="7" stroke="#fff"/><circle cx="110" cy="7" r="5" fill="#7b7eb2" stroke="#fff"/></svg>
  <p class="txt" style="left:0;width:1200px;top:106px;text-align:center;font-size:15px">Enim ad mini quis notrud exercitation ullamco laboris nisi ut aliqodo conseqin reprehenderit.</p>
  <div class="abs" style="left:265px;top:150px;width:75px;height:75px;border-radius:50%;background:#c9cbe0;border:2px solid #fff" role="img" aria-label="Customer portrait"></div>
  <p class="txt" style="left:358px;top:151px;font-size:16px;font-weight:700">Culpa qui officia deserunt mollitlorum.</p>
  <p class="txt" style="left:358px;top:178px;font-size:15px;line-height:25px;width:590px">Enim ad mini quis notrud exercitation ullaco laboris nisi ut aliqoido conseqin reprehderit in voluptate velit essle cillum dolore.</p>
  <svg class="abs" style="left:128px;top:110px" width="16" height="24"><path d="M12 2L3 12l9 10" stroke="#fff" stroke-width="3" fill="none"/></svg>
  <svg class="abs" style="left:1054px;top:110px" width="16" height="24"><path d="M4 2l9 10-9 10" stroke="#fff" stroke-width="3" fill="none"/></svg>
</section>

<footer class="abs footer">
  <svg class="abs" style="left:130px;top:26px" width="12" height="16"><path d="M6 0a6 6 0 0 1 6 6c0 4-6 10-6 10S0 10 0 6a6 6 0 0 1 6-6z" fill="#fff"/><circle cx="6" cy="6" r="2" fill="#2a2660"/></svg>
  <p class="abs" style="left:152px;top:23px;line-height:21px">Contrary to popular belief,<br>Lorem Ipsum is.<br>1234567</p>
  <svg class="abs" style="left:376px;top:24px" width="16" height="60"><path d="M2 1l4 0 1 4-2 1c1 2 2 3 4 4l1-2 4 1v4c-7 0-12-5-12-12z" fill="#fff"/><rect x="1" y="25" width="14" height="8" fill="#fff"/><rect x="1" y="46" width="14" height="10" fill="none" stroke="#fff" stroke-width="1.5"/><path d="M1 46l7 6 7-6" stroke="#fff" fill="none" stroke-width="1.5"/></svg>
  <p class="abs" style="left:406px;top:23px;line-height:21px">Phone: 123 456 789<br>Fax: 123 456 789<br>info@sitename.com</p>
  <span class="soc" style="left:601px"></span><span class="soc" style="left:646px"></span><span class="soc" style="left:691px"></span>
  <div class="abs" style="left:782px;top:32px;display:flex;align-items:center;gap:12px;font-size:38px;line-height:1"><span style="width:30px;height:30px;border-radius:50%;background:#fff"></span>Prairie Bio</div>
</footer>
<div class="abs copy">Copyright © 2014 Prairie Bio. All Rights Reserved.</div>

</body>
</html>
```